Boost Your Rankings - Search Engine Website

I am launching an SEO website and I am looking to have the site designed. There are a total of 8-10 pages that will need to be designed. I am providing 2 pages off the bat and will work with a designer once these 2 pages are complete. I have never posted a contest for website design (only logos, brochures, etc) so please let me know if there is anything you need from me. I am uploading 2 versions of our logo - a horizontal and a vertical version. I was thinking of getting these rendered in 3d, but I am just going with these for now. I am hoping to complete all work in 10 days, so hopefully the right design for the 1st 2 pages are submitted promptly.

We provide search engine optomization tools and backlinking tools. We provide free research tools as well as cost effective packages for SEO.

I am including 2 word files that have info about the home page and keyword summary page. Additional pages will include: Keyword Research Summary, The Que, Reports, etc.

I am also uploading a zip file that has some examples of home pages that I like. None of them are exactly what I am looking for, but they have certain elements that I like.

I am looking for a clean design and stands out and has good use of color.

Link to instructions files (2...more will be uploaded as first 2 pages are finalized): https://www.filevanta.net/sh/k4m2w7r9x3q5z8/Lp_Tn-7uy2

Forgot to include our logos. Here is a drop box link to the logos: 

https://www.filevanta.net/sh/93jd7fw2mx8qzpa/4Hy_Wq8eTn

big and small businesses, resellers

Seo

• see attached MS Word files for details about requirements.

```html
<!DOCTYPE html>
<html lang="en">
<head>
<meta charset="utf-8">
<title>Rankwell Ascent – Search Engine Rankings</title>
<link href="https://fonts.googleapis.com/css2?family=PT+Sans:wght@400;700&display=swap" rel="stylesheet">
<style>
:root{
  --blue:#1f4fae;
  --blue-dark:#173f8f;
  --navy:#1a3c8c;
  --orange:#f26a2d;
  --orange-light:#f7893c;
  --red:#e8461c;
  --green:#7cc242;
  --text:#333;
  --muted:#777;
  --rule:#e2e2e2;
  --footer:#262626;
  --footer-bottom:#1b1b1b;
  --footer-link:#8a8a8a;
  --white:#fff;
}
*{margin:0;padding:0;box-sizing:border-box}
html,body{width:776px;height:1200px;overflow:hidden}
body{font-family:"PT Sans",Arial,sans-serif;color:var(--text);background:#fff;font-size:8.5px;line-height:1.35;position:relative}
a{color:inherit;text-decoration:none}

.site-header{height:80px;background:linear-gradient(#fff,#ececec);position:relative}
.brand{position:absolute;left:78px;top:20px;display:flex;align-items:center;gap:8px}
.brand-mark{width:14px;height:14px;background:var(--orange);border-radius:50%}
.brand-name{font-size:24px;font-weight:700;color:var(--blue)}
.top-actions{position:absolute;right:76px;top:30px;display:flex;gap:8px}
.chip{height:20px;padding:0 9px;border-radius:3px;font-size:8.5px;display:flex;align-items:center;gap:5px}
.chip-light{background:linear-gradient(#fafafa,#ddd);border:1px solid #bbb;color:#333}
.chip-blue{background:linear-gradient(#3d66c4,var(--blue-dark));color:#fff}
.chip i{width:9px;height:9px;border-radius:2px;background:#f3b52a;display:inline-block}
.chip-blue i{background:#fff;opacity:.8}

.main-nav{height:31px;background:linear-gradient(var(--blue),var(--blue-dark));position:relative;display:flex;align-items:center;padding-left:78px}
.main-nav a{color:#9fc3ff;font-size:9.5px;margin-right:24px}
.main-nav a.active{color:var(--orange-light)}
.nav-buttons{position:absolute;right:76px;top:6px;display:flex;gap:6px}
.nav-btn{height:18px;padding:0 10px;border-radius:3px;font-size:8.5px;display:flex;align-items:center;gap:5px;color:#222}
.nav-btn.signup{background:linear-gradient(#4aa3f2,#1a6fc9);color:#fff}
.nav-btn.login{background:linear-gradient(#fbc46a,#f09a2a)}
.nav-btn i{width:8px;height:8px;border-radius:50%;background:#fff;display:inline-block}

.hero{height:256px;background:radial-gradient(circle at 35% 30%,var(--orange-light),var(--red) 75%);position:relative;color:#fff}
.hero h1{position:absolute;left:75px;top:30px;font-size:20px;line-height:1.05}
.hero h1 span{font-size:16px;display:block}
.hero-points{position:absolute;left:76px;top:84px;list-style:none;font-size:10px}
.hero-points li{display:flex;gap:6px;margin-bottom:8px;max-width:300px}
.hero-points svg{flex:none;margin-top:1px}
.hero-cta{position:absolute;left:76px;top:174px;display:flex;gap:11px}
.cta{width:139px;height:44px;border-radius:4px;font-size:17px;display:flex;align-items:center;justify-content:center}
.cta-buy{background:linear-gradient(#8fd04f,#5ea62a);color:#2e5a12;border:1px solid #4f8d20}
.cta-trial{background:linear-gradient(#3c82de,#1a55b4);color:#0d2d66;border:1px solid #164a9c}

.research-card{position:absolute;left:459px;top:35px;width:240px;height:182px;background:linear-gradient(#fff,#e3e3e3);box-shadow:0 4px 8px rgba(0,0,0,.25);padding:12px 11px}
.research-card h2{color:var(--red);font-size:15px;letter-spacing:-.2px;margin-bottom:6px}
.field{height:18px;background:linear-gradient(#bbb,#d2d2d2);border-radius:3px;margin-bottom:6px;font-size:8px;font-style:italic;color:#555;padding:3px 8px}
.check{display:flex;align-items:center;gap:5px;font-size:8px;color:var(--navy);margin-bottom:3px}
.check i{width:7px;height:7px;border:1px solid #999;background:#fff}
.search-btn{position:absolute;right:13px;bottom:12px;width:51px;height:20px;border-radius:3px;background:linear-gradient(#d9f04a,#95c21b);font-size:11px;font-weight:700;color:#224;display:flex;align-items:center;justify-content:center}

.content{position:absolute;top:367px;left:0;width:776px;height:598px}
.services{position:absolute;left:78px;top:34px;width:355px}
.section-title{font-size:17px;color:var(--navy);font-weight:700;margin-bottom:2px}
.intro{font-size:8px;color:#222;margin-bottom:10px}
.service{border-top:1px solid var(--rule);padding:10px 0 12px}
.service h3{color:var(--red);font-size:9px;font-weight:400;margin-bottom:2px}
.service p{font-size:8px;color:#555}
.service b{color:#222}

.sidebar{position:absolute;left:459px;top:22px;width:240px}
.tour-label{height:40px;margin-left:60px;background:linear-gradient(90deg,#f4f4f4,#e9e9e9);border-radius:4px}
.video{margin-top:10px;height:179px;background:linear-gradient(#e8ecef,#c9d0d6);position:relative}
.video-screen{position:absolute;inset:0 0 18px 0;background:linear-gradient(#eef1f3,#cfd6dc)}
.play{position:absolute;left:100px;top:66px;width:38px;height:38px;border-radius:50%;background:rgba(0,0,0,.75)}
.play:after{content:"";position:absolute;left:15px;top:11px;border-left:12px solid #fff;border-top:8px solid transparent;border-bottom:8px solid transparent}
.video-bar{position:absolute;left:0;right:0;bottom:0;height:18px;background:#222;display:flex;align-items:center;padding:0 6px;gap:6px;color:#ccc;font-size:7px}
.video-bar .track{flex:1;height:3px;background:#666;position:relative}
.video-bar .track:before{content:"";position:absolute;left:0;top:0;height:3px;width:18%;background:var(--red)}

.recent h2{font-size:17px;color:var(--navy);margin:22px 0 8px}
.post{display:flex;gap:8px;padding:8px 0;border-bottom:1px solid var(--rule);height:67px}
.post-photo{width:45px;height:45px;flex:none;background:linear-gradient(#b8a89a,#6c5b4f)}
.post h4{color:var(--red);font-size:9px;font-weight:400;line-height:1.2}
.post p{font-size:7.8px;color:#555;line-height:1.25}
.meta{display:flex;align-items:center;gap:3px;margin-top:3px;font-size:8px}
.meta .when{color:#2b8ed8;margin-right:4px}
.pill{height:10px;padding:0 3px;border:1px solid #bbb;border-radius:2px;font-size:6.5px;line-height:8px;color:#345;background:#f4f4f4}
.count{height:10px;padding:0 2px;border:1px solid #ccc;font-size:6.5px;line-height:8px;color:#333}
.pill.share{background:var(--red);color:#fff;border-color:var(--red)}
.view-all{text-align:right;font-size:9px;color:#555;margin-top:8px;display:flex;justify-content:flex-end;align-items:center;gap:5px}
.view-all i{width:9px;height:9px;background:var(--orange);border-radius:2px;display:inline-block}

.site-footer{position:absolute;top:965px;left:0;width:776px;height:200px;background:var(--footer);border-top:4px solid #e6e6e6}
.footer-col{position:absolute;top:20px}
.footer-col h5{color:#fff;font-size:13px;font-weight:400;margin-bottom:8px}
.footer-col a{display:block;font-size:7.5px;color:var(--footer-link);border-bottom:1px solid #3a3a3a;height:26px;line-height:26px;width:115px}
.footer-col a.hover{color:#ddd}
.newsletter{position:absolute;left:460px;top:0;height:200px;border-left:1px solid #3a3a3a;padding:20px 0 0 35px;width:316px}
.newsletter h5{color:#fff;font-size:13px;font-weight:400}
.newsletter small{color:var(--footer-link);font-size:7.5px}
.subscribe{display:flex;margin-top:6px;width:203px}
.subscribe span{flex:1;height:20px;background:#3b3b3b;font-size:7.5px;font-style:italic;color:#aaa;padding:4px 8px}
.subscribe b{width:48px;height:20px;background:linear-gradient(#f4f4f4,#ccc);color:#222;font-size:9px;display:flex;align-items:center;justify-content:center}
.follow{color:#fff;font-size:13px;margin-top:14px}
.social{display:flex;gap:4px;margin-top:8px;padding-bottom:10px;border-bottom:1px solid #3a3a3a;width:203px}
.social i{width:20px;height:20px;border-radius:50%;background:#cfcfcf;display:block}
.social i:first-child{background:#3b66b5}
.langs{display:flex;gap:5px;margin-top:10px}
.langs i{width:20px;height:13px;display:block}
.bottom-bar{position:absolute;top:1165px;left:0;width:776px;height:35px;background:var(--footer-bottom);color:#888;font-size:7.5px;display:flex;align-items:center;justify-content:space-between;padding:0 77px}
</style>
</head>
<body>

<header class="site-header">
  <div class="brand"><span class="brand-mark"></span><span class="brand-name">Rankwell Ascent</span></div>
  <div class="top-actions">
    <span class="chip chip-light"><i></i>Bookmark Us</span>
    <span class="chip chip-blue"><i></i>Login</span>
    <span class="chip chip-blue">Invite friends via FriendHub</span>
  </div>
</header>

<nav class="main-nav">
  <a class="active">About Us</a><a>Services</a><a>Features</a><a>Resources</a><a>Free Trial</a><a>FAQ</a><a>Contact Us</a>
  <div class="nav-buttons">
    <span class="nav-btn signup"><i></i>Sign up</span>
    <span class="nav-btn login"><i></i>Login</span>
  </div>
</nav>

<section class="hero">
  <h1>Boost Your Search Engine Rankings<span>Using Legal Back Linking Techniques.</span></h1>
  <ul class="hero-points">
    <li><svg width="12" height="10" viewBox="0 0 12 10"><path d="M0 3h6V0l6 5-6 5V7H0z" fill="#8fd04f"/></svg>Boost Rankings of your Business Webpage, VidStream Video, Social Media Page &amp; Blog</li>
    <li><svg width="12" height="10" viewBox="0 0 12 10"><path d="M0 3h6V0l6 5-6 5V7H0z" fill="#8fd04f"/></svg>Boost Pages from various websites</li>
    <li><svg width="12" height="10" viewBox="0 0 12 10"><path d="M0 3h6V0l6 5-6 5V7H0z" fill="#8fd04f"/></svg>Snapshots and Progress Reports of your search engine rankings</li>
  </ul>
  <div class="hero-cta">
    <a class="cta cta-buy">Buy Now</a>
    <a class="cta cta-trial">Free Trial</a>
  </div>
  <form class="research-card">
    <h2>FREE KEYWORD RESEARCH</h2>
    <div class="field">Enter Your URL</div>
    <div class="field">Enter Your Keywords</div>
    <div class="field">Type In Competitor URL</div>
    <div class="check"><i></i>Check Your Current Search Engine Ranking</div>
    <div class="check"><i></i>Research Keyword popularity and competitiveness</div>
    <div class="check"><i></i>See what your competitors are doing!</div>
    <span class="search-btn">Search</span>
  </form>
</section>

<main class="content">
  <section class="services">
    <h2 class="section-title">Services We Provide</h2>
    <p class="intro">Proin ac nulla in augue accumsan auctor. Integer ac lacinia erat. Etiam non tellus sit amet mi ornare ornare. Nulla lobortis vehicula lectus a euismod.</p>
    <div class="service"><h3>Website Analysis</h3><p><b>Sed id risus ut magna sodales consectetur.</b> Etiam nisl leo, gravida vel tempor vel, condimentum ac lectus. Etiam ut urna sed velit tristique eleifend ut bibendum leo.</p></div>
    <div class="service"><h3>Competitor Analysis</h3><p><b>Risus ut magna sodales consectetur.</b> Etiam nisl leo, gravida vel tempor vel, condimentum ac lectus. Etiam ut urna sed velit tristique eleifend ut bibendum leo. Aenean sed nisi felis. Mauris at ligula augue, quis ultricies purus. Suspendisse pellentesque turpis quis sem varius ultricies.</p></div>
    <div class="service"><h3>Keyword Selection</h3><p><b>Ut magna sodales consectetur.</b> Etiam nisl leo, gravida vel tempor vel, condimentum ac lectus. Etiam ut urna sed velit tristique eleifend ut bibendum leo. Aenean sed nisi felis.</p></div>
    <div class="service"><h3>Meta Optimization</h3><p><b>Magna sodales consectetur. Etiam nisl leo,</b> gravida vel tempor vel, condimentum ac lectus. Etiam ut urna sed velit tristique eleifend ut bibendum leo. Aenean sed nisi felis. Mauris at ligula augue, quis ultricies purus. Suspendisse pellentesque turpis quis sem varius ultricies.</p></div>
    <div class="service"><h3>Link Building</h3><p><b>Consectetur. Etiam nisl leo, gravida vel tempor vel,</b> condimentum ac lectus. Etiam ut urna sed velit tristique eleifend ut bibendum leo. Aenean sed nisi felis. Mauris at ligula augue, quis ultricies purus. Suspendisse pellentesque turpis quis sem varius ultricies.</p></div>
    <div class="service"><h3>SearchCo Authentication and Site Map Creation &amp; Submission</h3><p><b>Etiam nisl leo, gravida vel tempor vel, condimentum ac lectus.</b> Etiam ut urna sed velit tristique eleifend ut bibendum leo. Aenean sed nisi felis. Mauris at ligula augue, quis ultricies purus. Suspendisse pellentesque turpis quis sem varius ultricies.</p></div>
    <div class="service"><h3>SearchCo Analytics Installation</h3><p><b>Gravida vel tempor vel, condimentum ac lectus.</b> Etiam ut urna sed velit tristique eleifend ut bibendum leo. Aenean sed nisi felis. Mauris at ligula augue, quis ultricies purus. Suspendisse pellentesque turpis quis sem varius ultricies.</p></div>
  </section>

  <aside class="sidebar">
    <div class="tour-label" role="img" aria-label="Handwritten caption: Have a Quick video tour"></div>
    <div class="video">
      <div class="video-screen" role="img" aria-label="Video preview of the ranking report dashboard"></div>
      <span class="play"></span>
      <div class="video-bar"><span>▶</span><span class="track"></span><span>00.00</span></div>
    </div>

    <section class="recent">
      <h2>Recent Posts</h2>
      <article class="post"><div class="post-photo" role="img" aria-label="Author photo"></div><div><h4>Curabitur tempus imperdiet metus ut</h4><p>Vestibulum ante ipsum primis in faucibus orci luctus et ultrices posuere cubilia Curae;</p><div class="meta"><span class="when">10 mins ago</span><span class="pill">Like</span><span class="count">26</span><span class="pill">Post</span><span class="count">97</span><span class="pill share">Share</span><span class="count">832</span></div></div></article>
      <article class="post"><div class="post-photo" role="img" aria-label="Author photo"></div><div><h4>Donec ac ipsum quam, at pretium tortor.</h4><p>In ut odio ut massa aliquet accumsan non vel mauris. Ut sollicitudin nunc sed mauris</p><div class="meta"><span class="when">31 mins ago</span><span class="pill">Like</span><span class="count">26</span><span class="pill">Post</span><span class="count">97</span><span class="pill share">Share</span><span class="count">832</span></div></div></article>
      <article class="post"><div class="post-photo" role="img" aria-label="Author photo"></div><div><h4 style="text-decoration:underline">Ut sollicitudin nunc sed mauris hendrerit</h4><p>Nascetur ridiculus mus. Donec ac ipsum quam, at pretium tortor. Etiam at mauris in</p><div class="meta"><span class="when">2 days ago</span><span class="pill">Like</span><span class="count">26</span><span class="pill">Post</span><span class="count">97</span><span class="pill share">Share</span><span class="count">832</span></div></div></article>
      <article class="post" style="border-bottom:0"><div class="post-photo" role="img" aria-label="Author photo"></div><div><h4>Aenean nec dapibus turpis.</h4><p>Etiam volutpat mi velit. Morbi vel justo massa. Cras nunc neque, rutrum et aliquet quis,</p><div class="meta"><span class="when">1 week ago</span><span class="pill">Like</span><span class="count">26</span><span class="pill">Post</span><span class="count">97</span><span class="pill share">Share</span><span class="count">832</span></div></div></article>
      <div class="view-all"><i></i>View All Blog Posts</div>
    </section>
  </aside>
</main>

<footer class="site-footer">
  <div class="footer-col" style="left:78px"><h5>Company</h5><a>About Us</a><a class="hover">Why Rankwell Ascent</a><a>Affiliate Program</a><a>Tips To Using Our System</a><a>FAQ</a></div>
  <div class="footer-col" style="left:216px"><h5>Services</h5><a>Link Building</a><a>Local SEO</a><a>Free Trial</a><a>Free Keyword Analysis Tools</a><a>VidStream Video Marketing</a></div>
  <div class="footer-col" style="left:359px"><h5>SEO</h5><a>SEO Basics</a><a>SEO Tips</a><a>On Page SEO</a><a>Off Page SEO</a></div>
  <div class="newsletter">
    <h5>Sign up for Newsletter</h5>
    <small>Subscribe today to receive our free newsletter.</small>
    <div class="subscribe"><span>Enter your email address</span><b>Submit</b></div>
    <div class="follow">Follow Us On</div>
    <div class="social"><i></i><i></i><i></i><i></i><i></i><i></i></div>
    <div class="langs">
      <i style="background:linear-gradient(#b22234 50%,#eee 50%)"></i>
      <i style="background:#1f3a93"></i>
      <i style="background:linear-gradient(#1f3a93,#c8102e)"></i>
      <i style="background:linear-gradient(#f4923a 33%,#fff 33% 66%,#138808 66%)"></i>
      <i style="background:linear-gradient(#d21034 33%,#007a4d 33% 66%,#1f3a93 66%)"></i>
      <i style="background:linear-gradient(90deg,#1f3a93 33%,#fff 33% 66%,#e0202b 66%)"></i>
    </div>
  </div>
</footer>
<div class="bottom-bar"><span>© Copyright 2013 Rankwell Ascent. All Rights Reserved.</span><span>Privacy Policy &nbsp;|&nbsp; Terms &amp; Condition</span></div>

</body>
</html>
```